7th Annual Falcon Invitational Flyer

Looking to design an updated eye catching flyer maybe with someone movement, sound, and color. Below is an attachment of the flyer I have used in the past. I need to add color, sound, and movement to the flyer. This is an advertisement for youth folk style wrestling. You may contact me directly at 252-381-4926 if you need additional information. I really like the colors music and movement in the video below.
https://www.vidmarlo.com/watch?v=qT4kLmPzw8e

Target Market(s)

Youth Wrestling

Font styles to use
Serif

Colors
EB3D1F
EC4F4E
F09395
F8D3D4
FCEDEE

Requirements
Must have
• All information included on flyer.
Nice to have
• Color, sound, and movement

```html
<!DOCTYPE html>
<html lang="en">
<head>
<meta charset="utf-8">
<title>7th Annual Falcon Invitational</title>
<link rel="stylesheet" href="https://fonts.googleapis.com/css2?family=UnifrakturCook:wght@700&family=Rye&family=Poppins:wght@400;500;600;700&family=Oswald:wght@500&family=Merriweather:wght@700&display=swap">
<style>
:root{
  --page:#fbf3cf;
  --dark:#1e140d;
  --brown:#3a2517;
  --gold:#f3cf63;
  --gold-light:#fff1b8;
  --orange:#e2862a;
  --rust:#9c3a1a;
  --rust-deep:#7e2c12;
  --cream:#f4e9d8;
  --grey:#6e625a;
}
*{margin:0;padding:0;box-sizing:border-box}
html,body{width:923px;height:1200px;overflow:hidden;background:var(--page);font-family:"Poppins",sans-serif}
.flyer{position:absolute;left:67px;top:90px;width:789px;height:1021px;overflow:hidden;color:var(--cream);
  background:linear-gradient(180deg,#2a1a10 0%,#5a3418 28%,#7a4a22 40%,#3d2616 62%,#1c130c 100%);
  box-shadow:0 4px 18px rgba(0,0,0,.35)}
.backdrop{position:absolute;inset:0;background:radial-gradient(ellipse at 50% 35%,rgba(220,130,50,.35),transparent 60%),radial-gradient(ellipse at 30% 80%,rgba(120,70,30,.35),transparent 60%)}
.helmet-art{position:absolute;right:0;top:0;width:222px;height:230px;background:radial-gradient(ellipse at 55% 45%,#5c4a3a 0%,#2e221a 55%,rgba(60,20,10,0) 80%),linear-gradient(160deg,rgba(140,40,20,.5),rgba(0,0,0,0))}
.abs{position:absolute}
.logo{left:44px;top:46px;width:126px;text-align:center}
.logo-name{font:700 14px "Merriweather",serif;color:#fff}
.logo-mark{width:44px;height:44px;border-radius:50%;background:#fff;margin:6px auto}
.logo-sub{font:700 7px/1.2 "Merriweather",serif;color:#fff;text-transform:uppercase}
.edition{left:195px;top:48px;font:400 64px/1 "Rye",serif;color:var(--gold-light);text-shadow:0 2px 0 #8a5a10;white-space:nowrap}
.edition sup{font-size:36px;vertical-align:26px}
.title{left:48px;top:134px;font:700 58px/1 "UnifrakturCook",serif;color:var(--gold);text-shadow:0 2px 0 #6a4a10;white-space:nowrap}
.curve{left:0;top:205px;width:789px;height:200px}
.date{left:0;width:789px;top:266px;text-align:center;font:600 31px/1 "Poppins",sans-serif;color:var(--cream);white-space:nowrap}
.date .month{display:inline-block;background:var(--rust);color:var(--gold);padding:3px 12px;border-radius:14px 0 0 14px}
.date .day{display:inline-block;background:var(--brown);color:var(--gold);padding:3px 6px;border-radius:14px;margin-left:-6px}
.venue{left:186px;top:308px;font:500 17px/1.3 "Poppins",sans-serif}
.venue b{font-weight:700}
.pin{left:162px;top:316px}
.start{height:43px;display:flex;align-items:center;background:rgba(80,60,50,.75);border-radius:20px;font:500 15px/1.05 "Poppins",sans-serif;padding-left:12px}
.start .time{margin-left:auto;height:43px;display:flex;align-items:center;padding:0 18px;background:var(--brown);border-radius:18px;font:500 28px "Oswald",sans-serif;color:var(--gold)}
.start-young{left:53px;top:359px;width:316px}
.start-older{left:381px;top:359px;width:347px}
.register{left:57px;top:412px;font:500 21px "Poppins",sans-serif}
.fees{left:53px;top:447px;width:529px}
.fee-row{display:flex;height:27px;margin-bottom:5px;font:500 12.5px/27px "Poppins",sans-serif}
.fee-name{width:160px;background:var(--grey);padding-left:18px;border-radius:10px 0 0 10px}
.fee-cost{width:72px;background:var(--dark);text-align:center;font-weight:600}
.fee-deadline{flex:1;background:rgba(60,30,20,.8);color:var(--orange);padding-left:9px}
.fee-deadline b{font-weight:700}
.fee-time{width:88px;margin-left:3px;text-align:center;border:1px solid var(--cream);border-radius:3px;font-weight:600}
.fee-time.hot{background:var(--orange)}
.fee-time.mid{background:var(--grey)}
.fee-time.late{background:var(--rust)}
.badge{left:590px;top:426px;width:132px;height:132px}
.badge-text{left:590px;top:458px;width:132px;text-align:center;font:500 12.5px/1.25 "Poppins",sans-serif}
.badge-text strong{display:block;font:700 21px/1 "Poppins",sans-serif;color:var(--gold)}
.badge-text em{font-style:normal;font-weight:700;font-size:11px}
.card-note{left:57px;top:545px;font:400 12.5px "Poppins",sans-serif}
.card-note b{font-weight:700}
h2{font:700 15px "Merriweather",serif;color:var(--gold);letter-spacing:.3px}
.divisions{left:54px;top:577px;width:420px}
.divisions p{font:400 9.6px/18px "Poppins",sans-serif;color:#fff;white-space:nowrap}
.divisions p.wrap{line-height:12px;margin:3px 0;white-space:normal;width:400px}
.divisions p b{font-weight:600}
.divisions h2.girls{margin-top:10px}
.notes{left:52px;top:832px;width:340px;font:600 10px/1.25 "Poppins",sans-serif;color:var(--gold)}
.notes p+p{margin-top:4px}
.weighins{left:484px;top:577px;width:276px}
.wcards{display:flex;gap:4px;margin-top:6px}
.wcard{width:89px;height:98px;border-radius:8px 8px 6px 6px;text-align:center;color:var(--cream);overflow:hidden;background:#5a3a2e}
.wcard.w2{background:#6b5550}
.wcard.w3{background:#6a6360}
.wdate{font:500 11px/1 "Poppins",sans-serif;padding-top:14px}
.wdate span{display:block;font-size:18px;font-weight:600}
.wtime{font:500 10px/1.2 "Poppins",sans-serif;padding:2px 0;margin-top:2px}
.w1 .wtime{background:var(--rust-deep)}
.w2 .wtime{background:#9a857e}
.w3 .wtime{background:var(--orange)}
.wtime i{display:block;font-style:normal;font-size:5px;line-height:4px}
.wsub{font:400 6px/1.25 "Poppins",sans-serif;padding:5px 3px 0}
.rules{list-style:none;margin-top:12px;width:245px}
.rules li{position:relative;padding-left:13px;font:400 8.6px/1.25 "Poppins",sans-serif;margin-bottom:10px;color:#fff}
.rules li::before{content:"";position:absolute;left:1px;top:3px;width:6px;height:6px;border-radius:50%;background:var(--gold)}
.admission{left:179px;top:883px;width:431px;height:39px;background:var(--rust);border-radius:10px;display:flex;align-items:center;font:700 20px "Merriweather",serif;color:var(--cream)}
.admission .label{padding-left:14px}
.admission .price{margin:0 10px;height:46px;padding:0 9px;border-radius:50%;background:radial-gradient(var(--gold-light),var(--gold));color:var(--dark);font:500 24px/46px "Poppins",sans-serif}
.admission .price sup{font-size:12px}
.contact{left:61px;top:936px}
.contact p{font:400 12.5px "Poppins",sans-serif;color:var(--gold)}
.contact .director{display:flex;align-items:center;gap:5px;margin-top:2px;font:700 21px "Poppins",sans-serif;color:#fff}
.hotels{left:413px;top:936px;width:330px}
.hotels h3{font:700 13px "Poppins",sans-serif;color:var(--gold)}
.hotel-list{display:flex;justify-content:space-between}
.hotel b{display:block;font:600 13px "Poppins",sans-serif}
.hotel span{display:flex;align-items:center;gap:3px;font:500 11.5px "Poppins",sans-serif}
</style>
</head>
<body>
<div class="flyer">
  <div class="backdrop" role="img" aria-label="Dusky battlefield scene in warm brown and orange tones"></div>
  <div class="helmet-art" role="img" aria-label="Warrior helmet with red crest and cape"></div>

  <svg class="abs curve" viewBox="0 0 789 200" aria-hidden="true">
    <path d="M0 72 C60 32 200 24 390 26 L400 16 L410 26 C600 24 730 32 789 72 L789 200 L0 200Z" fill="rgba(30,20,12,.55)"/>
    <path d="M0 72 C60 32 200 24 390 26 L400 16 L410 26 C600 24 730 32 789 72" fill="none" stroke="#e9dcc6" stroke-width="2"/>
  </svg>

  <div class="abs logo">
    <div class="logo-name">TRYWA</div>
    <div class="logo-mark"></div>
    <div class="logo-sub">Tar Region Youth<br>Wrestling Association</div>
  </div>

  <div class="abs edition">7<sup>TH</sup> ANNUAL</div>
  <div class="abs title">Falcon Invitational</div>

  <div class="abs date">SATURDAY <span class="month">JANUARY</span><span class="day">25</span> 2025</div>

  <svg class="abs pin" width="26" height="26" viewBox="0 0 24 24" aria-hidden="true"><path d="M12 2a6 6 0 0 0-6 6c0 4.5 6 10 6 10s6-5.5 6-10a6 6 0 0 0-6-6zm0 8.5A2.5 2.5 0 1 1 12 5.5a2.5 2.5 0 0 1 0 5z" fill="#f3cf63"/><ellipse cx="12" cy="20" rx="8" ry="2.5" fill="none" stroke="#f3cf63" stroke-width="1.5"/></svg>
  <div class="abs venue"><b>Pinecrest Event Center</b><br>418 Harbor Ridge Rd, Marlow, NC 27851</div>

  <div class="abs start start-young"><span>4U, 6U, 8U, 10U<br>Wrestling Starts at</span><span class="time">8:30 AM</span></div>
  <div class="abs start start-older"><span>12U, Middle School, &amp; High<br>School&nbsp; Wrestling Starts at</span><span class="time">1:00 PM</span></div>

  <div class="abs register">Register @ www.matentry.com</div>

  <div class="abs fees">
    <div class="fee-row"><span class="fee-name">Early Registration</span><span class="fee-cost">$30.00</span><span class="fee-deadline">Deadline is <b>January 19, 2025</b></span><span class="fee-time hot">AT 11:59PM</span></div>
    <div class="fee-row"><span class="fee-name">Regular Registration</span><span class="fee-cost">$40.00</span><span class="fee-deadline">Deadline is <b>January 22, 2025</b></span><span class="fee-time mid">AT 11:59PM</span></div>
    <div class="fee-row"><span class="fee-name">Late Registration</span><span class="fee-cost">$50.00</span><span class="fee-deadline">Deadline is <b>January 24, 2025</b></span><span class="fee-time late">AT 5:00PM</span></div>
  </div>

  <svg class="abs badge" viewBox="0 0 100 100" aria-hidden="true"><polygon fill="#9c3a1a" points="50,0 58,6 67,3 72,11 82,11 84,20 93,23 91,32 98,38 94,46 100,53 94,60 97,69 89,73 89,82 80,84 77,93 68,92 62,99 54,95 46,100 39,94 30,97 26,89 17,88 16,79 7,75 9,66 2,60 7,52 0,45 7,39 4,30 12,26 13,17 22,15 25,6 34,7 40,0"/></svg>
  <div class="abs badge-text">Registration is<br>limited to the<strong>FIRST 500</strong><em>WRESTLERS</em></div>

  <div class="abs card-note">Non-TRYWA Card Holders will pay an additional <b><sup>$</sup>5.00 at weigh-ins.</b></div>

  <div class="abs divisions">
    <h2>BOYS DIVISIONS:</h2>
    <p><b>4 &amp; Under</b> - 30, 40, 50, HWT</p>
    <p><b>6 &amp; Under</b> - 36, 40, 44, 48, 52, 56, 60, HWT</p>
    <p><b>8 &amp; Under</b> - 40, 44, 48, 52, 56, 60, 64, 68, 72, 76, 80, 84, 88, 92, HWT</p>
    <p><b>10 &amp; Under</b> - 52, 56, 60, 64, 68, 72, 76, 80, 84, 88, 92, 96, 100, 110, HWT</p>
    <p><b>12 &amp; Under</b> - 64, 68, 72, 76, 80, 84, 88, 92, 96, 100, 105, 110, 115, 120, 130, 140, 160, HWT</p>
    <p><b>Middle School</b> - 72, 76, 80, 88, 92, 96, 100, 105, 110, 115, 120, 130, 140, 160, 210, HWT</p>
    <p><b>High School</b> - 106, 113, 120, 126, 132, 138, 144, 150, 157, 165, 175, 190, 215, HWT</p>
    <h2 class="girls">GIRLS DIVISIONS:</h2>
    <p><b>K-5</b> - 36, 40, 44, 48, 52, 56, 60, 64, 68, 72, 76, 80, 84, 88, 92, 96, 100, 110, 120,HWT</p>
    <p class="wrap"><b>Middle School</b> – 72, 76, 83, 90, 98, 106, 113, 120, 126, 132, 138, 145, 152, 160, 170, 182, 190, 220, HWT</p>
    <p><b>Women’s High School</b> 100, 107, 114, 120, 126, 132, 145, 152, 165, 185, HWT</p>
  </div>

  <div class="abs notes">
    <p>*Age is based upon wrestler’s age as of December 31, 2024.</p>
    <p>Tournament director has the right to combine weight classes if deemed necessary.</p>
  </div>

  <div class="abs weighins">
    <h2>WEIGH-INS:</h2>
    <div class="wcards">
      <div class="wcard w1"><div class="wdate">JANUARY<span>24, 2025</span></div><div class="wtime">5:00 PM<i>TO</i>7:00 PM</div><div class="wsub">(EARLY WEIGH-INS -<br><b>$10</b> CASH DUE AT SCALE)</div></div>
      <div class="wcard w2"><div class="wdate">JANUARY<span>25,2025</span></div><div class="wtime">6:00 PM<i>TO</i>7:30 PM</div><div class="wsub">(4U, 6U, 8U, 10U)</div></div>
      <div class="wcard w3"><div class="wdate">JANUARY<span>25,2025</span></div><div class="wtime">11:00 AM<i>TO</i>12:00 PM</div><div class="wsub">(12 &amp; UNDER, MS, &amp;<br>HIGH SCHOOL)</div></div>
    </div>
    <ul class="rules">
      <li>Tenths are waived/dropped at weigh-ins. Satellite weigh-ins will not be allowed.</li>
      <li>High School Divisions are given 2 lbs. growth allowance.</li>
      <li>Custom medals will be given to the top 3 individual finishers in each bracket.</li>
      <li>Custom Awards will be awarded to the top 4 teams. Referee decisions will be final.</li>
      <li>Riverbend Athletics is not responsible for accidents, injuries, or theft during the tournament.</li>
    </ul>
  </div>

  <div class="abs admission"><span class="label">ADMISSION:</span><span class="price"><sup>$</sup>10.00</span><span>PER PERSON</span></div>

  <div class="abs contact">
    <p>For More Information, contact Tournament Director</p>
    <div class="director">Dale Hutchins
      <svg width="24" height="24" viewBox="0 0 24 24" aria-hidden="true"><circle cx="12" cy="12" r="12" fill="#f3cf63"/><path d="M8 6l2.5 3-1.2 1.5c.8 1.8 2.2 3.2 4 4l1.5-1.2 3 2.5-1.5 2c-4.5-.5-9-5-9.5-9.5z" fill="#1e140d"/></svg>
      (252) 381-4926</div>
  </div>

  <div class="abs hotels">
    <h3>Hotels Available On-Site</h3>
    <div class="hotel-list">
      <div class="hotel"><b>Lakeside Suites</b><span><svg width="10" height="10" viewBox="0 0 24 24" aria-hidden="true"><circle cx="12" cy="12" r="12" fill="#f3cf63"/><path d="M8 6l2.5 3-1.2 1.5c.8 1.8 2.2 3.2 4 4l1.5-1.2 3 2.5-1.5 2c-4.5-.5-9-5-9.5-9.5z" fill="#1e140d"/></svg>(252) 410-2275</span></div>
      <div class="hotel"><b>Oakmont Inn</b><span><svg width="10" height="10" viewBox="0 0 24 24" aria-hidden="true"><circle cx="12" cy="12" r="12" fill="#f3cf63"/><path d="M8 6l2.5 3-1.2 1.5c.8 1.8 2.2 3.2 4 4l1.5-1.2 3 2.5-1.5 2c-4.5-.5-9-5-9.5-9.5z" fill="#1e140d"/></svg>(252) 410-6618</span></div>
      <div class="hotel"><b>Carriage House</b><span><svg width="10" height="10" viewBox="0 0 24 24" aria-hidden="true"><circle cx="12" cy="12" r="12" fill="#f3cf63"/><path d="M8 6l2.5 3-1.2 1.5c.8 1.8 2.2 3.2 4 4l1.5-1.2 3 2.5-1.5 2c-4.5-.5-9-5-9.5-9.5z" fill="#1e140d"/></svg>(252) 410-3394</span></div>
    </div>
  </div>
</div>
</body>
</html>
```